Business Card - connecting 2 souls and beggining the journey of self discovery

Logo on the front
with tag line

On the back list of services and contact details

Seminars
workshops
Coaching
podcasts

Daniel Porthwick
Health & Wellbeing Life Coach
0491 372 815
daniel@wovenpathwellness.example
wovenpathwellness.example

Industry/Entity Type

Life Coaching

Contact Information for Business Card

I like the use of colour from the logo to be used. I'm not a fan of white.

Requirements
Must have
• My tagline: The journey home starts with you
Nice to have
• Use of colour that is in the mind body soul logo

```html
<!DOCTYPE html>
<html lang="en">
<head>
<meta charset="utf-8">
<title>Woven Path Wellness – Business Card</title>
<link rel="stylesheet" href="https://fonts.googleapis.com/css2?family=Open+Sans:wght@400;600;700&display=swap">
<style>
  :root {
    --bg: #2b2c2e;
    --grey-light: #c9cacc;
    --grey-dark: #7c7d80;
    --white: #ffffff;
    --paper: #f6f6f6;
    --ink-grey: #7a7b7e;
    --green-top: #8fca55;
    --green-bottom: #4bb58a;
    --orange: #f2a03d;
    --purple: #9b59c6;
    --dot: #5cc08a;
    --mark: #f08a4b;
  }
  * { margin: 0; padding: 0; box-sizing: border-box; }
  html, body { width: 1200px; height: 900px; overflow: hidden; }
  body {
    background: var(--bg);
    font-family: "Open Sans", Arial, sans-serif;
    position: relative;
  }
  .card {
    position: absolute;
    width: 700px;
    height: 400px;
    border-radius: 3px;
    overflow: hidden;
    box-shadow: 0 10px 30px rgba(0,0,0,0.45);
  }
  /* Front */
  .card-front {
    left: 60px; top: 50px;
    background: linear-gradient(100deg, var(--grey-light) 0%, #a9aaac 45%, var(--grey-dark) 100%);
    color: var(--white);
    display: flex; flex-direction: column; align-items: center;
  }
  .brand-mark {
    width: 96px; height: 96px; border-radius: 50%;
    background: var(--mark);
  }
  .card-front .brand-mark { margin-top: 72px; }
  .card-front .brand-name {
    margin-top: 28px;
    font-size: 34px; font-weight: 600; letter-spacing: -1px;
  }
  .services {
    margin-top: 26px;
    list-style: none; display: flex; gap: 8px;
    font-size: 15px; font-weight: 400;
  }
  .services li { display: flex; align-items: center; gap: 8px; }
  .services li + li::before {
    content: ""; width: 6px; height: 6px; border-radius: 50%;
    background: var(--dot);
  }
  /* Back */
  .card-back {
    left: 440px; top: 470px;
    background: var(--paper);
  }
  .back-art { position: absolute; inset: 0; }
  .identity {
    position: absolute; left: 40px; top: 110px;
  }
  .card-back .brand-mark { width: 84px; height: 84px; margin-left: 40px; }
  .card-back .brand-name {
    margin-top: 18px;
    font-size: 28px; font-weight: 600; letter-spacing: -1px;
    color: var(--ink-grey);
  }
  .tagline {
    font-size: 16px; font-weight: 600; color: var(--ink-grey);
    margin-top: -2px;
  }
  .contact {
    position: absolute; right: 26px; top: 108px;
    text-align: right; color: var(--white);
  }
  .person-name { font-size: 22px; font-weight: 700; text-transform: uppercase; letter-spacing: 0.3px; }
  .person-role { font-size: 16px; font-weight: 700; text-transform: uppercase; line-height: 1.25; margin-bottom: 8px; }
  .contact-list { list-style: none; font-size: 14px; line-height: 1.5; }
  .contact-list li { display: flex; justify-content: flex-end; align-items: center; gap: 8px; }
  .contact-list svg { width: 13px; height: 13px; fill: var(--white); flex: none; }
</style>
</head>
<body>

<section class="card card-front">
  <div class="brand-mark"></div>
  <h1 class="brand-name">Woven Path Wellness</h1>
  <ul class="services">
    <li>Seminars</li>
    <li>Workshops</li>
    <li>Coaching</li>
    <li>Podcasts</li>
  </ul>
</section>

<section class="card card-back">
  <svg class="back-art" viewBox="0 0 700 400" preserveAspectRatio="none" aria-hidden="true">
    <defs>
      <linearGradient id="greenPanel" x1="0" y1="0" x2="0.4" y2="1">
        <stop offset="0" stop-color="#8fca55"/>
        <stop offset="1" stop-color="#4bb58a"/>
      </linearGradient>
    </defs>
    <path d="M300,0 C390,50 370,180 342,270 C326,330 322,375 330,400 L700,400 L700,0 Z" fill="#9b59c6"/>
    <path d="M325,0 C410,55 388,185 360,275 C344,335 340,378 346,400 L700,400 L700,0 Z" fill="#f2a03d"/>
    <path d="M340,0 C422,60 398,190 370,280 C355,338 350,380 356,400 L700,400 L700,0 Z" fill="#ffffff"/>
    <path d="M346,0 C428,62 403,192 375,282 C360,340 355,381 361,400 L700,400 L700,0 Z" fill="url(#greenPanel)"/>
  </svg>

  <div class="identity">
    <div class="brand-mark"></div>
    <h2 class="brand-name">Woven Path Wellness</h2>
    <p class="tagline">The journey home starts with you</p>
  </div>

  <div class="contact">
    <p class="person-name">Daniel Porthwick</p>
    <p class="person-role">Health<br>Wellbeing Life Coach</p>
    <ul class="contact-list">
      <li>0491 372 815
        <svg viewBox="0 0 24 24"><path d="M6.6 10.8a15.1 15.1 0 0 0 6.6 6.6l2.2-2.2c.3-.3.7-.4 1-.2 1.1.4 2.3.6 3.6.6.6 0 1 .4 1 1V20c0 .6-.4 1-1 1A17 17 0 0 1 3 4c0-.6.4-1 1-1h3.5c.6 0 1 .4 1 1 0 1.3.2 2.5.6 3.6.1.3 0 .7-.2 1z"/></svg>
      </li>
      <li>daniel@wovenpathwellness.example
        <svg viewBox="0 0 24 24"><path d="M2 5h20v14H2z M2 5l10 8 10-8" fill="none" stroke="#fff" stroke-width="2"/><path d="M2 5h20l-10 8z"/></svg>
      </li>
      <li>www.wovenpathwellness.example
        <svg viewBox="0 0 24 24"><circle cx="12" cy="12" r="10"/><path d="M2 12h20M12 2c3 3 3 17 0 20M12 2c-3 3-3 17 0 20" fill="none" stroke="#4bb58a" stroke-width="1.5"/></svg>
      </li>
    </ul>
  </div>
</section>

</body>
</html>
```